Marlow Yardcraft need a flyer - A6 - Double sided

We need a flyer that will engage potential customer in need for gardening services. We offer high quality gardening services spanning from lawn mowing and weeding to soil improvement to tree pruning and so on.
I would like a double sided flyer A6 size. I trust your expert touch in terms of lay out but the general idea I had was to have one side with the logo, a catchy picture (or more), the website/phone number/address and on the flip side a little more text focusing on the client perspective with statement such as 'Let us do the hard work so that you can enjoy your garden' (obviously the wording isn't my strongest skill) but the idea is to get into the customer perspective;
I would also like to list all the service we can offer such as but not limited to weeding, pruning, lawn care, green waste disposal, soil improvement, hedging, edging, lawn mowing,...
Happy for you to use any picture free of right from the internet if necessary

Target Market(s)

Home owner & Businesses

Industry/Entity Type

Landscape Gardening

Requirements
Must have
• website - http://yardcraft-marlow.com.au (feel free to browse the website to get ideas on color theme and overall look)
• phone number - (08) 6341 2705
Nice to have
• a list of services on offer
• phone number and website
• being customer perspective focused (the benefits for the customer) - perhaps on the flip side some text like 'highly trained and experienced landscape gardeners so that the job is done perfectly every time', 'always carrying all range of commercial grade tools so that we can tackle any job', 'Experienced gardeners so that the job is achieve faster' (it doesn't have to be in those exact words as I trust that you may be expert in wording as well as designers?)

```html
<!DOCTYPE html>
<html lang="en">
<head>
<meta charset="utf-8">
<title>Marlow Yardcraft – A6 Flyer</title>
<link rel="stylesheet" href="https://fonts.googleapis.com/css2?family=Nunito+Sans:wght@400;600;800;900&family=Open+Sans:wght@400&family=Kaushan+Script&display=swap">
<style>
  :root{
    --backdrop:#b8996e;
    --charcoal:#26302b;
    --lime:#9dc23f;
    --forest:#3d5a3c;
    --mist:#c8c9cb;
    --white:#ffffff;
    --ink:#1a1a1a;
  }
  *{box-sizing:border-box;margin:0;padding:0}
  html,body{width:1200px;height:1000px;overflow:hidden}
  body{background:var(--backdrop);position:relative;font-family:"Nunito Sans",Arial,sans-serif}

  .flyer{position:absolute;top:110px;width:552px;height:778px;overflow:hidden}
  .flyer--front{left:28px;background:var(--charcoal)}
  .flyer--back{left:620px;background:var(--white)}

  /* front */
  .brand-block{position:absolute;left:0;top:0;width:552px;height:216px;display:flex;flex-direction:column;justify-content:center;align-items:center}
  .brand-name{font-family:"Nunito Sans",Arial,sans-serif;font-weight:900;color:var(--white);text-align:center;line-height:.95;letter-spacing:-1px}
  .brand-name .line1{display:block;font-size:92px}
  .brand-name .line2{display:block;font-size:70px}
  .tagline-band{position:absolute;left:0;top:216px;width:552px;height:45px;background:var(--lime);color:var(--white);font-weight:800;font-size:18px;letter-spacing:.3px;display:flex;align-items:center;justify-content:center}
  .hero-photo{position:absolute;left:0;top:261px;width:552px;height:387px;
    background:linear-gradient(180deg,#a9c6dd 0%,#d7e4ea 22%,#6f8f4e 45%,#4f7a2e 62%,#7fb04a 82%,#5c8f2e 100%)}
  .contact-panel{position:absolute;left:0;top:648px;width:552px;height:130px;background:var(--mist);padding:6px 0 0 26px}
  .contact-heading{font-family:"Kaushan Script",cursive;font-size:23px;color:var(--charcoal)}
  .contact-list{list-style:none;margin-top:2px}
  .contact-list li{display:flex;align-items:center;gap:9px;color:var(--white);font-weight:800;font-size:16.5px;line-height:24px}
  .contact-list svg{width:15px;height:15px;flex:none}
  .social-squares{position:absolute;left:486px;top:18px;display:flex;flex-direction:column;gap:10px}
  .social-squares span{width:39px;height:39px;background:var(--charcoal);display:block}

  /* back */
  .pitch{position:absolute;left:0;top:0;width:552px;height:227px;background:var(--charcoal);padding:32px 26px 0}
  .pitch p{color:var(--white);font-weight:800;font-size:23px;line-height:31px}
  .pitch p + p{margin-top:14px}
  .pitch .brand-mini{margin-top:12px;font-weight:900;font-size:21px;line-height:22px;color:var(--white);width:140px}

  .services{position:absolute;left:0;top:227px;width:552px;height:551px;display:grid;grid-template-columns:repeat(3,184px);grid-template-rows:184px 184px 183px}
  .service{display:flex;flex-direction:column;align-items:center;justify-content:flex-end;padding-bottom:16px;font-family:"Open Sans",Arial,sans-serif;font-size:17px;line-height:19px;color:var(--ink);text-align:center}
  .service--forest{background:var(--forest)}
  .service--white{background:var(--white)}
  .service--mist{background:var(--mist)}
  .service--lime{background:var(--lime)}
  .service-icon{width:110px;height:90px;margin-bottom:14px;background:var(--ink);border-radius:6px;opacity:.85}
  .service--empty{background:var(--white)}
</style>
</head>
<body>

<section class="flyer flyer--front">
  <div class="brand-block">
    <h1 class="brand-name"><span class="line1">MARLOW</span><span class="line2">YARDCRAFT</span></h1>
  </div>
  <div class="tagline-band">AFFORDABLE AND RELIABLE GARDENING SERVICE</div>
  <div class="hero-photo" role="img" aria-label="Photograph of a lawn mower on freshly cut grass under trees and blue sky"></div>
  <div class="contact-panel">
    <p class="contact-heading">Get in touch today!</p>
    <ul class="contact-list">
      <li><svg viewBox="0 0 16 16"><path fill="#26302b" d="M3 3h10l2 4H1zM4 8h8v6H4z"/><circle cx="8" cy="11" r="1.6" fill="#c8c9cb"/></svg>(08) 6341 2705</li>
      <li><svg viewBox="0 0 16 16"><circle cx="8" cy="8" r="7" fill="#26302b"/><path d="M1 8h14M8 1c-3 3-3 11 0 14M8 1c3 3 3 11 0 14" stroke="#c8c9cb" stroke-width="1" fill="none"/></svg>www.yardcraft-marlow.com.au</li>
      <li><svg viewBox="0 0 16 16"><rect x="3" y="1" width="10" height="15" fill="#26302b"/><rect x="5" y="3" width="2" height="2" fill="#c8c9cb"/><rect x="9" y="3" width="2" height="2" fill="#c8c9cb"/><rect x="5" y="7" width="2" height="2" fill="#c8c9cb"/><rect x="9" y="7" width="2" height="2" fill="#c8c9cb"/></svg>Level 12, 40 Harlow Street Marlow WA 6000</li>
    </ul>
    <div class="social-squares" aria-hidden="true"><span></span><span></span></div>
  </div>
</section>

<section class="flyer flyer--back">
  <div class="pitch">
    <p>Don’t let your brown thumb get in the way of having a beautiful garden.</p>
    <p>Call in the professionals.</p>
    <div class="brand-mini">MARLOW YARDCRAFT</div>
  </div>
  <div class="services">
    <div class="service service--forest"><div class="service-icon" role="img" aria-label="Lawn mower icon"></div>Lawn Care</div>
    <div class="service service--white"><div class="service-icon" role="img" aria-label="Watering can over seedling icon"></div>Tree Pruning<br>and Plant Care</div>
    <div class="service service--mist"><div class="service-icon" role="img" aria-label="Chainsaw icon"></div>Hedge Trimming</div>
    <div class="service service--mist"><div class="service-icon" role="img" aria-label="Hand holding sprout icon"></div>Organic<br>Gardening</div>
    <div class="service service--lime"><div class="service-icon" role="img" aria-label="Wood chipper icon"></div>Mulching</div>
    <div class="service service--forest"><div class="service-icon" role="img" aria-label="Weeds and grass icon"></div>Weed Control</div>
    <div class="service service--lime"><div class="service-icon" role="img" aria-label="Wheelie bin icon"></div>Green Waste<br>Removal</div>
    <div class="service service--mist"><div class="service-icon" role="img" aria-label="Shovel in soil icon"></div>Fertilising and<br>Soil Improvement</div>
    <div class="service service--empty"></div>
  </div>
</section>

</body>
</html>
```